Fennick Executive Search - New Business Card Design Project

We are an executive search firm called Fennick Executive Search based in the UK. We require a custom design for a business card. We're looking to convey a professional service to executives for executive search recruitment services. In terms of colours, we like dark blues and grays (maybe even silver incorporated somewhere if we go for a foiled type of card) but we're open to your artistic flare. See our current logo in attachments. We are totally open on design so long as the design is slick and professional.
Updates

Thanks for all your contributions of various designs. I have to say the quality of work has been amazing which is going to make our job quite difficult in the coming days on making a decision. Thanks to you all that have taken the time to submit designs thus far. We'll keep on reviewing and try to narrow down our selection as soon as possible.

Target Market(s)

Executive Search

Industry/Entity Type

Recruitment

Contact Information for Business Card

Fennick Executive Search,
Exclusively Sourcing & Hiring Senior Leaders
Gordon Pellbury, Managing Director,
07823 906417
0117 486 7132
gordon@fennickexecutive.co.uk
fennickexecutive.co.uk
58 Lindmoor Court, Hatherley Road, Bristol, BS32 9QJ

Font styles to use
Sans Serif
Other font styles liked:
• Roboto (which is used in our logo)

Requirements
Must have
• Our logo (It has a subtle fade on it from #02071d at top to #333649 at bottom)
• The logo can be on one side or both sides
• Must be elegant and professional
• We have 2nd slogan CONSULT | INSPIRE | INNOVATE | DELIVER which can be incorporated into the card
Nice to have
• Use of blues and grey colours
• Compatible with similar styling to our website fennickexecutive.co.uk
Should not have
• Must not be overly brash
• Must not contain cartoon characters

```html
<!DOCTYPE html>
<html lang="en">
<head>
<meta charset="utf-8">
<title>Fennick Executive Search – Business Card</title>
<link rel="stylesheet" href="https://fonts.googleapis.com/css2?family=Roboto:wght@300;500&family=Open+Sans:wght@400;600;700&display=swap">
<style>
  :root {
    --page-bg: #e9e9ec;
    --card-top: #262a40;
    --card-bottom: #1b1e30;
    --silver: #a3a5b3;
    --silver-soft: #8d8fa0;
    --white: #ffffff;
    --rule: #9fa2b4;
  }
  * { box-sizing: border-box; margin: 0; padding: 0; }
  html, body {
    width: 1200px; height: 864px; overflow: hidden;
    background: var(--page-bg);
  }
  .canvas {
    position: relative; width: 1200px; height: 864px;
    display: flex; align-items: center; justify-content: center; gap: 40px;
  }
  .card {
    position: relative; width: 540px; height: 315px;
    background: linear-gradient(180deg, var(--card-top), var(--card-bottom));
    box-shadow: 0 10px 28px rgba(0,0,0,.25);
    overflow: hidden;
  }

  /* Wordmark: one line, one weight, one colour, plain square beside */
  .wordmark {
    position: absolute; display: flex; align-items: center;
    font-family: "Roboto", Arial, sans-serif; font-weight: 500;
    white-space: nowrap;
  }
  .wordmark-square { flex: none; }

  /* Front */
  .front-wordmark { left: 40px; top: 118px; gap: 14px; color: var(--silver); font-size: 33px; }
  .front-wordmark .wordmark-square { width: 22px; height: 22px; background: var(--silver); }
  .front-slogan {
    position: absolute; left: 40px; bottom: 34px;
    font-family: "Roboto", Arial, sans-serif; font-weight: 300;
    font-size: 12px; letter-spacing: 2px; color: var(--silver-soft);
  }

  /* Back */
  .back-wordmark { right: 30px; top: 34px; gap: 10px; color: var(--white); font-size: 22px; }
  .back-wordmark .wordmark-square { width: 14px; height: 14px; background: var(--white); }
  .back-tagline {
    position: absolute; right: 30px; top: 68px;
    font-family: "Open Sans", Arial, sans-serif; font-weight: 600;
    font-size: 10.5px; color: var(--white);
  }
  .contact-block {
    position: absolute; left: 30px; top: 100px;
    font-family: "Open Sans", Arial, sans-serif; color: var(--white);
  }
  .person-name { font-weight: 700; font-size: 14px; letter-spacing: .3px; text-transform: uppercase; line-height: 19px; }
  .person-role { font-weight: 400; font-size: 14px; letter-spacing: .3px; text-transform: uppercase; line-height: 19px; margin-bottom: 6px; }
  .contact-list { list-style: none; }
  .contact-list li {
    display: flex; align-items: center; gap: 8px;
    font-size: 13px; line-height: 18px;
  }
  .contact-list svg { width: 11px; height: 11px; fill: var(--white); flex: none; }
  .divider {
    position: absolute; left: 30px; right: 30px; top: 222px;
    height: 1px; background: var(--rule);
  }
  .address-rule {
    position: absolute; right: 30px; top: 236px; width: 150px;
    height: 1px; background: var(--rule);
  }
  .address {
    position: absolute; right: 30px; top: 242px; text-align: right;
    font-family: "Open Sans", Arial, sans-serif; font-size: 13px;
    line-height: 19px; color: var(--white); font-style: normal;
  }
</style>
</head>
<body>
<main class="canvas">

  <section class="card card-front" aria-label="Card front">
    <div class="wordmark front-wordmark">
      <span class="wordmark-square" aria-hidden="true"></span>
      <span class="wordmark-name">Fennick Executive Search</span>
    </div>
    <p class="front-slogan">CONSULT | INSPIRE | INNOVATE | DELIVER</p>
  </section>

  <section class="card card-back" aria-label="Card back">
    <div class="wordmark back-wordmark">
      <span class="wordmark-square" aria-hidden="true"></span>
      <span class="wordmark-name">Fennick Executive Search</span>
    </div>
    <p class="back-tagline">Exclusively Sourcing &amp; Hiring Senior Leaders</p>

    <div class="contact-block">
      <p class="person-name">Gordon Pellbury</p>
      <p class="person-role">Managing Director</p>
      <ul class="contact-list">
        <li>
          <svg viewBox="0 0 24 24" aria-hidden="true"><path d="M6.6 10.8a15.1 15.1 0 0 0 6.6 6.6l2.2-2.2a1 1 0 0 1 1-.25 11.4 11.4 0 0 0 3.6.57 1 1 0 0 1 1 1V20a1 1 0 0 1-1 1A17 17 0 0 1 3 4a1 1 0 0 1 1-1h3.5a1 1 0 0 1 1 1c0 1.25.2 2.45.57 3.57a1 1 0 0 1-.25 1z"/></svg>
          07823 906417
        </li>
        <li>
          <svg viewBox="0 0 24 24" aria-hidden="true"><path d="M4 5h16a2 2 0 0 1 2 2v12a2 2 0 0 1-2 2H4a2 2 0 0 1-2-2V7a2 2 0 0 1 2-2zm2 4v3h12V9zm0 5v2h3v-2zm5 0v2h3v-2zm5 0v2h2v-2zM7 2h10v2H7z"/></svg>
          0117 486 7132
        </li>
        <li>
          <svg viewBox="0 0 24 24" aria-hidden="true"><path d="M3 5h18a1 1 0 0 1 1 1v12a1 1 0 0 1-1 1H3a1 1 0 0 1-1-1V6a1 1 0 0 1 1-1zm9 7.5L4 7.5V9l8 5 8-5V7.5z"/></svg>
          gordon@fennickexecutive.co.uk
        </li>
        <li>
          <svg viewBox="0 0 24 24" aria-hidden="true"><path d="M12 2a10 10 0 1 0 0 20 10 10 0 0 0 0-20zm0 2c.9 1.2 1.6 2.5 2 4h-4c.4-1.5 1.1-2.8 2-4zM4.3 14a8 8 0 0 1 0-4h3.4a16 16 0 0 0 0 4zm.8 2h2.9c.3 1.3.8 2.5 1.5 3.6A8 8 0 0 1 5.1 16zM8 8H5.1a8 8 0 0 1 4.4-3.6C8.8 5.5 8.3 6.7 8 8zm4 12c-.9-1.2-1.6-2.5-2-4h4c-.4 1.5-1.1 2.8-2 4zm2.3-6H9.7a14 14 0 0 1 0-4h4.6a14 14 0 0 1 0 4zm.2 5.6c.7-1.1 1.2-2.3 1.5-3.6h2.9a8 8 0 0 1-4.4 3.6zM16.3 14a16 16 0 0 0 0-4h3.4a8 8 0 0 1 0 4zM16 8c-.3-1.3-.8-2.5-1.5-3.6A8 8 0 0 1 18.9 8z"/></svg>
          fennickexecutive.co.uk
        </li>
      </ul>
    </div>

    <div class="divider"></div>
    <div class="address-rule"></div>
    <address class="address">
      58 Lindmoor Court<br>
      Hatherley Road<br>
      Bristol, BS32 9QJ
    </address>
  </section>

</main>
</body>
</html>
```